Flyer Design Project

We are a start-up real estate brokerage looking to attract new agents. Our business relies heavily on technology to help give agents more time to spend with clients. Our model is also different from a typical broker in that we do not take a percentage of commission from each sale an agent makes. Instead we charge a simple flat monthly fee and the agent keeps 100% of the commission the earn.
The ideal flyer will be pleasing to the eye, should probably have some appropriate graphics, use our logo and project a modern yet sophisticated company image. This is and advertising flyer that will be followed up with a more detailed brochure (later project).
Updates

While I like the initial design I was looking for more of a change from my design.  Here are some clarifications:

The design should not included the "click" option so it can be used online or in print.  Instead include the site corvelliahomes.com/careers

I want more of a list of features with less description.  The list should have:
- Deal Tracker included
- No Commission Split
- No Floor Time... Leads sent directly to you
- E & O Insurance included
- All your listings showcased on Homefinda.com
- Showing appointment solution.

Some description of each can be included but less of a question answer style than what I originally had.
It does not need to be a straight list, the items all need to be mentioned somewhere on the flyer but not necessarily in a list style.
Maybe an image of business meeting or greeting (agent joining).

Please do not hesitate to ask questions for clarification

The image of meeting or greeting is optional - you choose what you think is best.
Also, use of the "About Us" that was uploaded my be a good idea.  - I'm not sure on this either

Target Market(s)

current real estate agents and people considering a real estate career

Industry/Entity Type

Real Estate

Requirements
Must have
• Should list that we include "Deal Tracker" which is considered the top program for real estate agents (info and logos can be found at dealtracker.com)
Should highlight our low cost structure ($350 per month) and no transaction fees.
Should highlight that no office time is required. We provide virtual office solutions to save time.
Our contact number (555) 482-9167 ext. 204
Nice to have
• Any other additional information from the attached flyers (which should not be used as a template as they all need to be designed in a later project).

```html
<!DOCTYPE html>
<html lang="en">
<head>
<meta charset="utf-8">
<title>Corvellia Homes – Agent Recruitment Flyer</title>
<link href="https://fonts.googleapis.com/css2?family=Arimo:wght@400;700&family=Open+Sans:wght@400;700&display=swap" rel="stylesheet">
<style>
  :root {
    --maroon: #7d2a2b;
    --ink: #1f1f1f;
    --ribbon-edge: #4a4a4a;
    --page-top: #ffffff;
    --page-bottom: #e9e9e9;
    --band-dark: #1c1c1c;
    --band-light: #8d8d8d;
    --white: #ffffff;
  }
  * { margin: 0; padding: 0; box-sizing: border-box; }
  html, body { width: 936px; height: 1200px; overflow: hidden; background: var(--white); }
  .flyer {
    position: relative; width: 936px; height: 1200px; overflow: hidden;
    font-family: "Arimo", Arial, sans-serif; color: var(--ink);
  }
  .page {
    position: absolute; left: 18px; top: 18px; width: 900px; height: 1164px;
    background: linear-gradient(180deg, var(--page-top) 0%, #f3f3f3 40%, var(--page-bottom) 100%);
  }
  .price-ribbon { position: absolute; left: 92px; top: 18px; width: 248px; height: 225px; }
  .price-ribbon svg { position: absolute; inset: 0; }
  .price-text { position: absolute; left: 0; top: 52px; width: 248px; text-align: center; color: var(--white); }
  .price-label { font-size: 17px; font-weight: 700; letter-spacing: .3px; }
  .price-amount { font-size: 66px; font-weight: 700; line-height: 58px; margin-top: 4px; }
  .price-unit { font-size: 16px; font-weight: 700; margin-top: 4px; }
  .price-note { font-size: 14px; font-weight: 400; margin-top: 6px; }
  .headline {
    position: absolute; left: 362px; top: 74px; font-size: 53px; font-weight: 700; line-height: 54px; color: var(--ink);
  }
  .subhead {
    position: absolute; left: 0; top: 280px; width: 936px; text-align: center;
    font-size: 35px; font-weight: 700; line-height: 42px; color: var(--maroon);
  }
  .feature {
    position: absolute; left: 118px; width: 700px; text-align: center;
    font-family: "Open Sans", Arial, sans-serif; font-size: 20px; line-height: 29px; color: var(--ink);
  }
  .feature strong { font-weight: 700; display: block; }
  .feature-split { top: 418px; }
  .feature-leads { top: 553px; }
  .feature-showings { top: 668px; left: 88px; width: 760px; }
  .cta-label {
    position: absolute; left: 0; top: 800px; width: 936px; text-align: center; font-size: 22px; font-weight: 700;
  }
  .cta-label .site { text-transform: none; }
  .phone-button {
    position: absolute; left: 292px; top: 837px; width: 355px; height: 74px;
    background: var(--maroon); border-radius: 7px; box-shadow: 5px 5px 0 var(--ink);
    color: var(--white); text-align: center;
  }
  .phone-number { font-size: 31px; font-weight: 700; margin-top: 9px; line-height: 34px; }
  .phone-ext { font-size: 17px; font-weight: 700; }
  .office-note { position: absolute; left: 0; top: 927px; width: 936px; text-align: center; }
  .office-title { font-size: 22px; font-weight: 700; }
  .office-sub { font-size: 16px; font-weight: 700; margin-top: 2px; }
  .footer-band {
    position: absolute; left: 18px; top: 988px; width: 900px; height: 194px;
    background: linear-gradient(90deg, var(--band-dark) 0%, var(--band-dark) 38%, #5a5a5a 62%, var(--band-light) 100%);
  }
  .brand-box {
    position: absolute; left: 84px; top: 50px; width: 310px; height: 93px;
    border: 3px solid #d8d8d8; background: #111; display: flex; align-items: center; justify-content: center;
    color: var(--white); font-size: 27px; font-weight: 400; letter-spacing: 1px; white-space: nowrap;
  }
  .crm-promo { position: absolute; left: 455px; top: 47px; width: 255px; color: var(--white); }
  .crm-title { font-size: 19px; font-weight: 700; }
  .crm-stat { font-size: 14px; line-height: 16px; margin-top: 4px; color: #f0f0f0; }
  .crm-detail { font-size: 9px; line-height: 11px; margin-top: 12px; color: #e8e8e8; }
  .device-art {
    position: absolute; left: 722px; top: 0; width: 178px; height: 194px;
    background: linear-gradient(160deg, #d9dde4 0%, #8fa4c0 45%, #2c2f36 100%);
  }
</style>
</head>
<body>
<div class="flyer">
  <div class="page"></div>

  <div class="price-ribbon">
    <svg width="248" height="225" viewBox="0 0 248 225" aria-hidden="true">
      <polygon points="0,0 248,0 248,225 124,188 0,225" fill="var(--ribbon-edge)"/>
      <polygon points="10,0 238,0 238,206 124,172 10,206" fill="var(--maroon)"/>
    </svg>
    <div class="price-text">
      <div class="price-label">LOW COST STRUCTURE</div>
      <div class="price-amount">$350</div>
      <div class="price-unit">per month</div>
      <div class="price-note">no transaction fees</div>
    </div>
  </div>

  <h1 class="headline">Keep 100% Of Your<br>Commission</h1>

  <h2 class="subhead">We are currently seeking new and<br>experienced agents to join our growing firm</h2>

  <p class="feature feature-split"><strong>No commission split. E&amp;O insurance included.</strong>There are no more commission splits, no transaction fees, and E&amp;O coverage is included. Pay just $350 per month and keep 100% of your commission.</p>

  <p class="feature feature-leads"><strong>No floor time. Leads sent directly to you.</strong>Our lead system feeds prospects to you anytime, anywhere. No more sitting in your broker’s office when over 80% of home buyers are online.</p>

  <p class="feature feature-showings"><strong>Showing appointment solution. Listings on Homefinda.com.</strong>Showings can be scheduled seven days a week, with the longest hours in the industry, and all your listings are showcased on Homefinda.com.</p>

  <div class="cta-label">CALL OR VISIT <span class="site">corvelliahomes.com/careers</span></div>
  <div class="phone-button">
    <div class="phone-number">(555) 482-9167</div>
    <div class="phone-ext">EXT. 204</div>
  </div>

  <div class="office-note">
    <div class="office-title">No Office Time is Required</div>
    <div class="office-sub">We Provide Virtual Office Solutions to Save Time</div>
  </div>

  <div class="footer-band">
    <div class="brand-box">CORVELLIA HOMES</div>
    <div class="crm-promo">
      <div class="crm-title">Deal Tracker CRM™ included</div>
      <div class="crm-stat">74% of clients will give you a referral if you stay in touch.</div>
      <div class="crm-detail">Build referrals and build your business with real estate’s most intuitive customer contact management (CRM) software for agents and brokers.</div>
    </div>
    <div class="device-art" role="img" aria-label="Phones and a tablet showing the contact management app"></div>
  </div>
</div>
</body>
</html>
```